Web Site for Strategy and Technology Consulting Company

We are looking for a website design that engages potential customers to understand our services and contact us. In this contest, we are looking for a homepage design, but the winning designer will be favored for the design of some of the more complicated interior pages of the site. An additional contest (or contests) for these pages will be added soon.

PLATROM AND RESPONSIVE DESIGN
The site will be implemented in WordPress using the Elementor page builder.
We are looking for a design that will look good on phones are well as laptop browsers.

UPLOADED FILES INCLUDE:
1a A wireframe of the homepage we are looking for. The Uploaded PDF also includes a draft of the text proposed for the homepage. Designers are free to go beyond the wireframe, but all elements of the wireframe should be included.
1b A Word document with the draft text of the homepage.
2a-d The Norvalith logo. Two versions are included – a dark version which works well against a light background, and a light version which works well against a dark background.
3 The Norvalith color palette with HEX and RGB values. Designers are not limited to this palette, but colors should be complementary.
4 A draft of the homepage menu
5 Service sheets with information on the services we provide

MORE ABOUT NORVALITH
Norvalith is a consulting company focused on transforming businesses through software. Our tagline, “Transformation Delivered,” recognizes the gap business often have between business transformation and the software they end up with. By listening to our customers and understanding their vision and where they are, we help get our customers where they want to go.

We increase our capability by working with many consultants and partners, allowing us to provide our customers with the best people and the software that best suits them.

Industry/Entity Type

Consulting

Number of Pages Required

1 page

Font styles to use
Sans Serif

Requirements
Must have
• the content represented on the wireframe uploaded
Nice to have
• interactive features, such as roll-over icons that reveal additional information

```html
<!DOCTYPE html>
<html lang="en">
<head>
<meta charset="utf-8">
<title>Norvalith – Transformation Delivered</title>
<link rel="stylesheet" href="https://fonts.googleapis.com/css2?family=DM+Sans:wght@400;500;700&display=swap">
<style>
:root{
  --navy:#25598f;
  --footer:#2b5c93;
  --ink:#1d2230;
  --muted:#555b66;
  --gold:#e3b51e;
  --gold-deep:#d6aa12;
  --olive:#8c8230;
  --slate:#45556e;
  --line:#9aa0a8;
  --white:#ffffff;
}
*{box-sizing:border-box;margin:0;padding:0}
html,body{width:1200px;height:3243px;overflow:hidden}
body{font-family:"DM Sans",sans-serif;color:var(--ink);background:var(--white);position:relative}
section,header,footer{position:absolute;left:0;width:1200px}

/* header */
.site-header{top:0;height:82px;background:var(--white)}
.brand{position:absolute;left:98px;top:20px;font-size:40px;font-weight:400;color:#4b5563;letter-spacing:-0.5px}
.brand-dot{display:inline-block;width:8px;height:8px;background:var(--navy);border-radius:50%;margin-right:4px;vertical-align:middle}
.main-nav{position:absolute;left:563px;top:34px;display:flex;gap:32px;font-size:13px;font-weight:500;color:var(--ink)}
.main-nav span::after{content:"";display:inline-block;width:5px;height:5px;border-right:2px solid var(--ink);border-bottom:2px solid var(--ink);transform:rotate(45deg);margin-left:7px;position:relative;top:-3px}
.btn-contact{position:absolute;left:980px;top:25px;width:122px;height:34px;background:var(--navy);color:#fff;font-size:13px;font-weight:500;display:flex;align-items:center;justify-content:center}

/* hero */
.hero{top:82px;height:612px;overflow:hidden}
.hero-photo{position:absolute;inset:0;background:linear-gradient(90deg,#1a2230 0%,#2c3444 35%,#4a4a50 60%,#3a3128 85%,#2a2420 100%)}
.hero-title{position:absolute;left:98px;top:142px;font-size:56px;line-height:60px;font-weight:700;color:#fff}
.hero-list{position:absolute;left:98px;top:272px;list-style:none;color:#fff;font-size:20px;line-height:36px}
.hero-list li{display:flex;align-items:center;gap:8px}
.btn-gold{position:absolute;background:var(--gold);color:var(--ink);font-size:15px;font-weight:500;display:flex;align-items:center;justify-content:center;gap:8px}
.hero .btn-gold{left:98px;top:429px;width:150px;height:42px}
.hero-wave{position:absolute;left:0;bottom:0;width:1200px;height:90px}

/* services */
.services{top:694px;height:640px}
.services h2{position:absolute;left:0;width:1200px;top:70px;text-align:center;font-size:34px;line-height:43px;font-weight:500}
.services-intro{position:absolute;left:180px;width:840px;top:174px;text-align:center;font-size:15px;line-height:26px;color:var(--muted)}
.card{position:absolute;top:303px;width:184px;height:248px;border:1px solid var(--line);text-align:center}
.card-icon{position:absolute;left:72px;top:20px;width:40px;height:42px}
.card-brand{position:absolute;left:0;width:100%;top:22px;font-size:18px;font-style:normal;font-weight:500;color:#5b6ee0}
.card h3{position:absolute;left:8px;right:8px;top:74px;font-size:15px;line-height:21px;font-weight:500}
.card p{position:absolute;left:12px;right:12px;top:120px;font-size:13px;line-height:19px;color:var(--muted)}
.card-btn{position:absolute;left:33px;top:188px;width:116px;height:31px;border:1px solid var(--line);font-size:13px;color:var(--muted);display:flex;align-items:center;justify-content:center}
.card-btn.is-active{background:var(--navy);border-color:var(--navy);color:#fff}

/* people */
.people{top:1333px;height:562px;background:var(--slate);color:#fff}
.people h2{position:absolute;left:98px;top:94px;font-size:33px;font-weight:700}
.people-body{position:absolute;left:98px;width:582px;font-size:15px;line-height:26px}
.people-points{position:absolute;left:98px;top:250px;width:600px;list-style:none;font-size:15px;font-weight:700;line-height:22px}
.people-points li{display:flex;gap:8px;margin-bottom:6px}
.people-points li svg{flex:none;margin-top:3px}
.people .btn-gold{left:99px;top:434px;width:150px;height:42px}
.people-photo{position:absolute;left:728px;top:0;width:472px;height:562px;background:linear-gradient(180deg,#f1f1f1 0%,#e3ddd6 55%,#7a6a58 85%,#4a3c30 100%)}

/* testimonials */
.testimonials{top:1895px;height:711px;background:#fff}
.testi-photo{position:absolute;left:184px;top:117px;width:342px;height:469px;background:linear-gradient(160deg,#9fb4c4 0%,#c7b49c 50%,#33475c 100%)}
.testi-badge{position:absolute;left:450px;top:163px;width:152px;height:152px;border-radius:50%;background:var(--gold);border:4px solid #f1d36a;text-align:center;font-size:13px;line-height:19px;font-weight:500;color:var(--ink);padding-top:56px}
.eyebrow{position:absolute;font-size:15px;font-weight:500;color:var(--gold-deep)}
.testimonials .eyebrow{left:672px;top:162px}
.testimonials h2{position:absolute;left:672px;top:185px;font-size:35px;line-height:43px;font-weight:500}
.quote-card{position:absolute;left:672px;top:305px;width:344px;height:205px;background:#fff;box-shadow:0 6px 24px rgba(0,0,0,0.1)}
.avatar{position:absolute;left:28px;top:20px;width:46px;height:46px;border-radius:50%;background:#b5a89a}
.quote-name{position:absolute;left:98px;top:36px;font-size:12px;font-weight:700;color:var(--navy)}
.quote-org{position:absolute;left:98px;top:52px;font-size:12px;color:var(--muted)}
.quote-text{position:absolute;left:29px;right:24px;top:98px;font-size:11px;line-height:17px;color:var(--muted)}
.quote-text b{color:var(--gold-deep)}
.slider-dots{position:absolute;display:flex;gap:8px;align-items:center}
.slider-dots i{display:block;width:6px;height:6px;background:var(--navy)}
.slider-dots i.is-active{width:12px;height:12px;border:2px solid var(--navy);background:#fff;box-shadow:inset 0 0 0 2px #fff,inset 0 0 0 6px var(--navy)}
.testimonials .slider-dots{left:970px;top:2330px;top:529px}

/* technologies */
.tech{top:2606px;height:290px;overflow:hidden}
.tech-photo{position:absolute;inset:0;background:linear-gradient(90deg,#23272d 0%,#2e3338 50%,#3a4b3f 80%,#23282b 100%)}
.tech .eyebrow{left:98px;top:43px}
.tech h2{position:absolute;left:98px;top:66px;font-size:33px;font-weight:700;color:#fff}
.tech-logos{position:absolute;left:98px;top:160px;width:1004px;display:flex;justify-content:space-between;align-items:center;color:#fff;font-size:22px;font-weight:500}
.tech .slider-dots{left:578px;top:236px;gap:5px}
.tech .slider-dots i{width:6px;height:6px;border-radius:50%;background:#d8d8d8;border:none;box-shadow:none}
.tech .slider-dots i.is-active{background:var(--gold)}

/* footer */
.site-footer{top:2896px;height:347px;background:var(--footer);color:#fff}
.footer-brand{position:absolute;left:100px;top:70px;font-size:30px;font-weight:400}
.footer-about{position:absolute;left:101px;top:118px;width:420px;font-size:13px;line-height:22px}
.footer-col{position:absolute;top:72px}
.footer-col h4{font-size:17px;font-weight:700;margin-bottom:14px}
.footer-col p{font-size:14px;line-height:22px}
.footer-address{left:613px}
.footer-hello{left:869px}
.footer-email{display:inline-block;padding-bottom:6px;border-bottom:1px solid #fff;width:203px}
.footer-phone{margin-top:12px;font-size:17px!important}
.socials{display:flex;gap:10px;margin-top:12px}
.socials span{width:36px;height:36px;border:1px solid #fff;border-radius:50%;display:block}
.footer-rule{position:absolute;left:98px;top:262px;width:1004px;height:1px;background:rgba(255,255,255,0.4)}
.footer-links{position:absolute;left:98px;top:300px;font-size:13px}
.footer-copy{position:absolute;right:98px;top:300px;font-size:13px}
</style>
</head>
<body>

<header class="site-header">
  <div class="brand"><span class="brand-dot"></span>Norvalith</div>
  <nav class="main-nav"><span>ABOUT US</span><span>SERVICES</span><span>INSIGHTS</span><span>JOIN US</span></nav>
  <div class="btn-contact">CONTACT US</div>
</header>

<section class="hero">
  <div class="hero-photo" role="img" aria-label="Photo of business colleagues in conversation, one holding a tablet"></div>
  <h1 class="hero-title">Transformation<br>Delivered.</h1>
  <ul class="hero-list">
    <li><svg width="20" height="16" viewBox="0 0 20 16"><path d="M2 8l5 5L18 2" fill="none" stroke="#e3b51e" stroke-width="3"/></svg>Transformation Planning &amp; Support</li>
    <li><svg width="20" height="16" viewBox="0 0 20 16"><path d="M2 8l5 5L18 2" fill="none" stroke="#e3b51e" stroke-width="3"/></svg>Discover, connect, and trust your data.</li>
    <li><svg width="20" height="16" viewBox="0 0 20 16"><path d="M2 8l5 5L18 2" fill="none" stroke="#e3b51e" stroke-width="3"/></svg>ERP Solutions</li>
    <li><svg width="20" height="16" viewBox="0 0 20 16"><path d="M2 8l5 5L18 2" fill="none" stroke="#e3b51e" stroke-width="3"/></svg>CRM Solutions</li>
  </ul>
  <div class="btn-gold">OUR STORY <svg width="18" height="18" viewBox="0 0 18 18"><circle cx="9" cy="9" r="7.5" fill="none" stroke="#1d2230" stroke-width="1.5"/><path d="M7.5 5.5L11 9l-3.5 3.5" fill="none" stroke="#1d2230" stroke-width="1.5"/></svg></div>
  <svg class="hero-wave" viewBox="0 0 1200 90" preserveAspectRatio="none">
    <path d="M0 62 C200 30 380 40 560 58 C760 78 900 80 1200 40 L1200 90 L0 90Z" fill="#8c8230"/>
    <path d="M0 72 C200 46 380 54 560 70 C760 88 900 88 1200 52 L1200 90 L0 90Z" fill="#ffffff"/>
  </svg>
</section>

<section class="services">
  <h2>Transformation Supported<br>by Technology</h2>
  <p class="services-intro">During our early years, Norvalith focused only on business transformation. We came to realize that successful transformation often depended on quality software implementations, and often more than one. Now we focus on five things, the five things most businesses need to reach their goals.</p>

  <div class="card" style="left:98px">
    <svg class="card-icon" viewBox="0 0 40 42"><rect x="6" y="4" width="26" height="34" fill="none" stroke="#5b6ee0" stroke-width="1.5"/><path d="M11 12h16M11 18h16M11 24h16M11 30h10" stroke="#5b6ee0" stroke-width="1.5"/></svg>
    <h3>Business<br>Transformation</h3>
    <p>Define and execute your strategy.</p>
    <div class="card-btn">Know More</div>
  </div>
  <div class="card" style="left:303px">
    <svg class="card-icon" viewBox="0 0 40 42"><rect x="4" y="6" width="32" height="26" fill="none" stroke="#5b6ee0" stroke-width="1.5"/><circle cx="20" cy="19" r="6" fill="none" stroke="#5b6ee0" stroke-width="1.5"/><path d="M14 38h12M20 32v6" stroke="#5b6ee0" stroke-width="1.5"/></svg>
    <h3>ERP<br>Solutions</h3>
    <p>Assess, upgrade, and implement ERP solutions to meet your needs.</p>
    <div class="card-btn is-active">Know More</div>
  </div>
  <div class="card" style="left:507px">
    <svg class="card-icon" viewBox="0 0 40 42"><rect x="6" y="8" width="24" height="30" fill="none" stroke="#5b6ee0" stroke-width="1.5"/><path d="M11 16h14M11 22h14M11 28h8" stroke="#5b6ee0" stroke-width="1.5"/><circle cx="31" cy="30" r="5" fill="none" stroke="#5b6ee0" stroke-width="1.5"/></svg>
    <h3>CRM<br>Solutions</h3>
    <p>Take your relationship to the next level.</p>
    <div class="card-btn">Know More</div>
  </div>
  <div class="card" style="left:712px">
    <svg class="card-icon" viewBox="0 0 40 42"><rect x="4" y="6" width="32" height="24" fill="none" stroke="#5b6ee0" stroke-width="1.5"/><path d="M10 24v-6M15 24v-10M20 24v-4" stroke="#5b6ee0" stroke-width="1.5"/><circle cx="28" cy="16" r="4" fill="none" stroke="#5b6ee0" stroke-width="1.5"/><path d="M20 30v8M14 38h12" stroke="#5b6ee0" stroke-width="1.5"/></svg>
    <h3>Data and Business<br>Intelligence</h3>
    <p>Discover, connect, and trust your data.</p>
    <div class="card-btn">Know More</div>
  </div>
  <div class="card" style="left:917px">
    <div class="card-brand">Uplift</div>
    <h3>Building the Right<br>Team of People</h3>
    <p>Hire resources for your transformation journey.</p>
    <div class="card-btn">Know More</div>
  </div>
</section>

<section class="people">
  <h2>It’s the People</h2>
  <p class="people-body" style="top:156px">The world has changed in the past twenty years. The people you need might not all work for one company. Our clients want the best resources, available quickly. That’s why, in addition to our team of experts, we partner with:</p>
  <ul class="people-points">
    <li><svg width="16" height="16" viewBox="0 0 16 16"><circle cx="8" cy="8" r="8" fill="#e3b51e"/><path d="M4.5 8l2.5 2.5 4.5-5" fill="none" stroke="#45556e" stroke-width="1.8"/></svg>A large network of expert consultants who are the best at what they do,</li>
    <li><svg width="16" height="16" viewBox="0 0 16 16"><circle cx="8" cy="8" r="8" fill="#e3b51e"/><path d="M4.5 8l2.5 2.5 4.5-5" fill="none" stroke="#45556e" stroke-width="1.8"/></svg>Service providers all over the world to provide the resources and<br>value that are right for you, available 24 x 7.</li>
  </ul>
  <p class="people-body" style="top:346px">People are invariably at the center of our customer’s success. Find out how we can add our experts to yours.</p>
  <div class="btn-gold">OUR TEAM <svg width="18" height="18" viewBox="0 0 18 18"><circle cx="9" cy="9" r="7.5" fill="none" stroke="#1d2230" stroke-width="1.5"/><path d="M7.5 5.5L11 9l-3.5 3.5" fill="none" stroke="#1d2230" stroke-width="1.5"/></svg></div>
  <div class="people-photo" role="img" aria-label="Photo of a smiling diverse team gathered around a table with laptops"></div>
</section>

<section class="testimonials">
  <div class="testi-photo" role="img" aria-label="Photo of a consultant in a suit shaking hands with a client"></div>
  <div class="testi-badge">We’ve More<br>Then 1234+ Global<br>Clients</div>
  <div class="eyebrow">Clients Testimonials</div>
  <h2>Amazing Feedback Say<br>About Services</h2>
  <div class="quote-card">
    <div class="avatar" role="img" aria-label="Client portrait"></div>
    <div class="quote-name">MARA ELLISON, PRESIDENT</div>
    <div class="quote-org">Brightline Fixtures</div>
    <p class="quote-text"><b>“</b> Norvalith quickly moved us past talking about what needed to be done, to doing it. Development projects are never easy and when things got tough in the first phase of development, Norvalith stepped in to right the ship and put us on a new course. <b>”</b></p>
  </div>
  <div class="slider-dots"><i></i><i class="is-active"></i><i></i></div>
</section>

<section class="tech">
  <div class="tech-photo" role="img" aria-label="Photo of a person reviewing data dashboards on a screen"></div>
  <div class="eyebrow">Technologies</div>
  <h2>Rotator of Technologies</h2>
  <div class="tech-logos">
    <span>Corvane Suite</span><span>Ledgerwise</span><span>Pipeflow</span><span>Quantora BI</span><span>Frostbase</span><span>Vizmetric</span>
  </div>
  <div class="slider-dots"><i></i><i class="is-active"></i><i></i><i></i></div>
</section>

<footer class="site-footer">
  <div class="footer-brand">Norvalith</div>
  <p class="footer-about">We do more for our customers than implement software. We listen. We work to understand where they are in their transformation journey and where they want to go. We partner with them to clear the roadblocks that stand in their way, ensuring they reach their destination.</p>
  <div class="footer-col footer-address">
    <h4>Address</h4>
    <p>400 Lakeview Plaza<br>Suite 210, Riverton, MN<br>55012</p>
    <div class="socials"><span></span><span></span></div>
  </div>
  <div class="footer-col footer-hello">
    <h4>Say Hello</h4>
    <p><span class="footer-email">hello@norvalithconsulting.com</span></p>
    <p class="footer-phone">(555) 301-2290</p>
  </div>
  <div class="footer-rule"></div>
  <div class="footer-links">Offerings &nbsp;|&nbsp; Capabilities &nbsp;|&nbsp; Industries &nbsp;|&nbsp; Team &nbsp;|&nbsp; About</div>
  <div class="footer-copy">© 2023 Norvalith Consulting. All Rights Reserved.</div>
</footer>

</body>
</html>
```